I'm an electrician and the name of my company is called Brisk 'N' Bright Electrical. I require a professional business card that speaks to my clients, I also need it to be innovative and modern. We do maintenance & service work for domestic and commercial premises.

Industry/Entity Type

Electrical

Contact Information for Business Card

Must have the name of my company Brisk 'N' Bright Electrical, my name Darren Kolovich and my contact details 0427 318 592 and company email address Brisknbrightelectrical@quillpost.example and/or website Brisknbrightelectrical.example.au

Logo Text

Brisk 'N' Bright Electrical (If possible)

Colors
33a6d7
0592cd
3176b5

```html
<!DOCTYPE html>
<html lang="en">
<head>
<meta charset="utf-8">
<title>Brisk 'N' Bright Electrical – Business Card</title>
<link href="https://fonts.googleapis.com/css2?family=Montserrat:wght@300;400;700&display=swap" rel="stylesheet">
<style>
  :root {
    --backdrop: #2b2b2b;
    --card-light: #ffffff;
    --card-dark: #0b0b0b;
    --band: #0d0d0d;
    --band-accent: #5c5c5c;
    --ink: #222222;
    --ink-on-dark: #ffffff;
    --muted: #8a8a8a;
    --contact: #b9b9b9;
    --silver: #c4c4c4;
  }
  * { box-sizing: border-box; margin: 0; padding: 0; }
  html, body {
    width: 1189px; height: 1200px; overflow: hidden;
    background: var(--backdrop);
    font-family: "Montserrat", sans-serif;
  }
  .canvas { position: relative; width: 1189px; height: 1200px; }

  .card {
    position: absolute; left: 261px; width: 668px; height: 380px;
    border-radius: 18px; overflow: hidden;
  }
  .card--front { top: 172px; background: var(--card-light); }
  .card--back  { top: 649px; background: var(--card-dark); }

  .company-name {
    position: absolute; left: 0; right: 0;
    text-align: center; font-weight: 700; font-size: 36px; letter-spacing: 0.2px;
    white-space: nowrap;
  }
  .card--front .company-name { top: 112px; color: var(--ink); }
  .card--back  .company-name { top: 168px; color: var(--silver); }

  .contact-band {
    position: absolute; left: 0; top: 238px; width: 649px; height: 99px;
    background: var(--band);
  }
  .band-accent {
    position: absolute; left: 653px; top: 238px; width: 15px; height: 99px;
    background: var(--band-accent);
  }

  .identity {
    position: absolute; right: 370px; top: 20px; text-align: right; white-space: nowrap;
  }
  .identity__name { font-weight: 700; font-size: 27px; color: var(--ink-on-dark); line-height: 1.2; }
  .identity__role { font-weight: 400; font-size: 15px; color: var(--muted); margin-top: 2px; }

  .divider {
    position: absolute; left: 296px; top: 23px; width: 2px; height: 50px;
    background: var(--ink-on-dark);
  }

  .contact-list {
    position: absolute; left: 312px; top: 17px; list-style: none;
  }
  .contact-list li {
    display: flex; align-items: center; gap: 8px; height: 20px;
    font-weight: 300; font-size: 13.5px; color: var(--contact); white-space: nowrap;
  }
  .contact-list svg { width: 12px; height: 12px; flex: none; fill: var(--ink-on-dark); }
</style>
</head>
<body>
<main class="canvas">

  <section class="card card--front" aria-label="Business card front">
    <h1 class="company-name">Brisk 'N' Bright Electrical</h1>

    <div class="contact-band">
      <div class="identity">
        <p class="identity__name">Darren Kolovich</p>
        <p class="identity__role">Electrician</p>
      </div>
      <span class="divider"></span>
      <ul class="contact-list">
        <li>
          <svg viewBox="0 0 24 24" aria-hidden="true"><path d="M6.6 10.8a15.1 15.1 0 0 0 6.6 6.6l2.2-2.2c.3-.3.7-.4 1-.2 1.1.4 2.3.6 3.6.6.6 0 1 .4 1 1V20c0 .6-.4 1-1 1A17 17 0 0 1 3 4c0-.6.4-1 1-1h3.5c.6 0 1 .4 1 1 0 1.3.2 2.5.6 3.6.1.3 0 .7-.2 1z"/></svg>
          0427 318 592
        </li>
        <li>
          <svg viewBox="0 0 24 24" aria-hidden="true"><path d="M12 2a10 10 0 1 0 5 18.7l-1-1.7A8 8 0 1 1 20 12v1.2c0 1-.7 1.8-1.6 1.8s-1.6-.8-1.6-1.8V7.5h-1.9v.9A5 5 0 1 0 15.6 16a3.5 3.5 0 0 0 2.8 1.3c2 0 3.6-1.8 3.6-4.1V12A10 10 0 0 0 12 2zm0 13a3 3 0 1 1 0-6 3 3 0 0 1 0 6z"/></svg>
          brisknbrightelectrical@quillpost.example
        </li>
        <li>
          <svg viewBox="0 0 24 24" aria-hidden="true"><path d="M12 2a10 10 0 1 0 0 20 10 10 0 0 0 0-20zm6.9 6h-2.9a15.6 15.6 0 0 0-1.4-3.6A8 8 0 0 1 18.9 8zM12 4c.8 1.2 1.5 2.5 1.9 4h-3.8c.4-1.5 1.1-2.8 1.9-4zM4.3 14a8.2 8.2 0 0 1 0-4h3.4a16.5 16.5 0 0 0 0 4zm.8 2h2.9c.3 1.3.8 2.5 1.4 3.6A8 8 0 0 1 5.1 16zM8 8H5.1a8 8 0 0 1 4.3-3.6C8.8 5.5 8.3 6.7 8 8zm4 12c-.8-1.2-1.5-2.5-1.9-4h3.8c-.4 1.5-1.1 2.8-1.9 4zm2.3-6H9.7a14.7 14.7 0 0 1 0-4h4.6a14.7 14.7 0 0 1 0 4zm.3 5.6c.6-1.1 1.1-2.3 1.4-3.6h2.9a8 8 0 0 1-4.3 3.6zm1.7-5.6a16.5 16.5 0 0 0 0-4h3.4a8.2 8.2 0 0 1 0 4z"/></svg>
          brisknbrightelectrical.example.au
        </li>
      </ul>
    </div>
    <span class="band-accent"></span>
  </section>

  <section class="card card--back" aria-label="Business card back">
    <h2 class="company-name">Brisk 'N' Bright Electrical</h2>
  </section>

</main>
</body>
</html>
```